Business Card for a Mortgage Agent (myself)

I need a business card for my new job as Mortgage Agent. The Broker's logo is to be on the card as well as the brokerage License number. Not sure if to include a photo or not. Info to be on card.
Dante Roux
Mortgage Agent
Lic # M47105386
Cell: 905-614-2753
Email: danterouxk.ma@fennmail.com
Web: www.karlvostermortgages.com
TPW Brokerage Lic. # 73918

```html
<!DOCTYPE html>
<html lang="en">
<head>
<meta charset="utf-8">
<title>Dante Roux – Business Card</title>
<link href="https://fonts.googleapis.com/css2?family=Open+Sans:wght@400;600;700&display=swap" rel="stylesheet">
<style>
  :root {
    --backdrop: #f4f08d;
    --card: #ffffff;
    --brand-blue: #0f52a0;
    --ink-blue: #17457f;
    --brand-yellow: #f9cc12;
  }
  * { margin: 0; padding: 0; box-sizing: border-box; }
  html, body { width: 856px; height: 1200px; overflow: hidden; }
  body {
    background: var(--backdrop);
    font-family: "Open Sans", Arial, sans-serif;
    color: var(--ink-blue);
    position: relative;
  }
  .card {
    position: absolute;
    left: 190px;
    width: 476px;
    height: 272px;
    background: var(--card);
    border-radius: 12px;
    overflow: hidden;
  }
  .card--front { top: 255px; }
  .card--back { top: 603px; }

  .accent-bar {
    position: absolute;
    left: 23px; top: 0;
    width: 25px; height: 97px;
    background: var(--brand-yellow);
    border-bottom: 5px solid var(--brand-blue);
  }
  .agent-name {
    position: absolute; left: 61px; top: 20px;
    font-size: 22px; font-weight: 700; letter-spacing: 0.2px;
    color: var(--ink-blue);
  }
  .agent-title {
    position: absolute; left: 61px; top: 56px;
    font-size: 16px; font-weight: 600;
  }
  .agent-licence {
    position: absolute; left: 61px; top: 84px;
    font-size: 14px; font-weight: 400;
  }

  .brand {
    position: absolute;
    display: flex; align-items: center; gap: 8px;
    color: var(--brand-blue);
    font-weight: 700;
  }
  .brand__square { background: var(--brand-yellow); flex: none; }
  .brand--small { left: 300px; top: 46px; font-size: 15px; line-height: 1.2; }
  .brand--small .brand__square { width: 26px; height: 26px; }
  .brand--large {
    left: 0; right: 0; top: 80px; justify-content: center;
    font-size: 26px; gap: 14px;
  }
  .brand--large .brand__square { width: 40px; height: 40px; }

  .contact-list { position: absolute; left: 20px; top: 138px; list-style: none; }
  .contact-list li {
    display: flex; align-items: center; height: 28px;
    font-size: 14px; font-weight: 600;
  }
  .contact-list svg { width: 30px; height: 28px; margin-right: 11px; flex: none; }

  .licence-band {
    position: absolute; left: 0; right: 0;
    height: 23px; line-height: 23px;
    text-align: center; font-size: 15px; font-weight: 600;
  }
  .licence-band--blue { top: 233px; background: var(--brand-blue); color: #fff; }
  .licence-band--yellow { top: 210px; background: var(--brand-yellow); color: var(--ink-blue); }
</style>
</head>
<body>
  <section class="card card--front">
    <div class="accent-bar"></div>
    <h1 class="agent-name">DANTE ROUX</h1>
    <p class="agent-title">Mortgage Agent</p>
    <p class="agent-licence">Lic # M47105386</p>

    <div class="brand brand--small">
      <span class="brand__square"></span>
      <span>TPW<br>Tallpine Wealth Partners</span>
    </div>

    <ul class="contact-list">
      <li>
        <svg viewBox="0 0 30 28" aria-hidden="true">
          <path d="M2 16 L14 28 L16 26 L4 14 Z" fill="var(--brand-blue)"/>
          <path d="M15 1 L28 14 L15 27 L2 14 Z" fill="var(--brand-yellow)"/>
          <rect x="11.5" y="8" width="7" height="12" rx="1.2" fill="none" stroke="var(--brand-blue)" stroke-width="1.4"/>
          <line x1="14" y1="18" x2="16" y2="18" stroke="var(--brand-blue)" stroke-width="1.2"/>
        </svg>
        905-614-2753
      </li>
      <li>
        <svg viewBox="0 0 30 28" aria-hidden="true">
          <path d="M2 16 L14 28 L16 26 L4 14 Z" fill="var(--brand-blue)"/>
          <path d="M15 1 L28 14 L15 27 L2 14 Z" fill="var(--brand-yellow)"/>
          <circle cx="15" cy="14" r="6" fill="none" stroke="var(--brand-blue)" stroke-width="1.3"/>
          <ellipse cx="15" cy="14" rx="2.6" ry="6" fill="none" stroke="var(--brand-blue)" stroke-width="1"/>
          <line x1="9" y1="14" x2="21" y2="14" stroke="var(--brand-blue)" stroke-width="1"/>
        </svg>
        www.karlvostermortgages.com
      </li>
      <li>
        <svg viewBox="0 0 30 28" aria-hidden="true">
          <path d="M2 16 L14 28 L16 26 L4 14 Z" fill="var(--brand-blue)"/>
          <path d="M15 1 L28 14 L15 27 L2 14 Z" fill="var(--brand-yellow)"/>
          <rect x="9.5" y="10" width="11" height="8" fill="none" stroke="var(--brand-blue)" stroke-width="1.3"/>
          <path d="M9.5 10 L15 14.5 L20.5 10" fill="none" stroke="var(--brand-blue)" stroke-width="1.1"/>
        </svg>
        danterouxk.ma@fennmail.com
      </li>
    </ul>

    <div class="licence-band licence-band--blue">TPW Brokerage Lic. # 73918</div>
  </section>

  <section class="card card--back">
    <div class="brand brand--large">
      <span class="brand__square"></span>
      <span>TPW Tallpine Wealth Partners</span>
    </div>
    <div class="licence-band licence-band--yellow">TPW Brokerage Lic. # 73918</div>
  </section>
</body>
</html>
```